Business Card Design Project

Business card design with a funky, clean, modern design. Business is an immigration consultancy. Client base will be Canadian employers wanting to hire or retain foreign workers and foreign nationals wanting to immigrate to Canada.

Full color possible, but should incorporate red/white/black as per the logo to be provided. Double sided card design.

Target Market(s)

Canadian employers looking to hire/retain staff and also foreign nationals immigrating to Canada

Industry/Entity Type

Business

Requirements
Must have
• Logo (to be provided)
Name (Marla Voskuil, Immigration Consultant)
Phone (604) 731-5562
E-mail: marla@tallowbrookmigration.example
Web: www.tallowbrookmigration.example

Nice to have
• Tag Line
Clean, modern style

```html
<!DOCTYPE html>
<html lang="en">
<head>
<meta charset="utf-8">
<title>Marla Voskuil – Business Card</title>
<link rel="stylesheet" href="https://fonts.googleapis.com/css2?family=Didact+Gothic&family=Open+Sans:wght@400;700&family=Crimson+Text:ital@1&display=swap">
<style>
  :root {
    --red: #c3121a;
    --red-deep: #8e0a10;
    --red-bright: #e8141f;
    --black: #161616;
    --ink: #1c1c1c;
    --card-light: #ffffff;
    --card-grey: #c6cbcb;
    --brand-tint: #e07b7b;
  }
  * { margin: 0; padding: 0; box-sizing: border-box; }
  html, body {
    width: 1200px; height: 741px; overflow: hidden; background: #ffffff;
  }
  .card {
    position: relative; width: 1200px; height: 741px; overflow: hidden;
    background: radial-gradient(ellipse 620px 420px at 620px 330px, var(--card-light) 0%, #e9ecec 45%, var(--card-grey) 100%);
    font-family: "Open Sans", sans-serif; color: var(--ink);
  }
  .waves { position: absolute; inset: 0; }
  .brand {
    position: absolute; left: 922px; top: 144px; width: 220px;
    text-align: center; font-family: "Open Sans", sans-serif; font-weight: 700;
    font-size: 21px; line-height: 1.15; letter-spacing: 1px; color: var(--brand-tint);
    text-transform: uppercase;
  }
  .name {
    position: absolute; left: 52px; top: 158px;
    font-family: "Didact Gothic", sans-serif; font-weight: 400; font-size: 86px; line-height: 1;
    letter-spacing: 2px; color: var(--black); white-space: nowrap;
  }
  .name .first { color: var(--red); }
  .title {
    position: absolute; left: 55px; top: 248px;
    font-weight: 700; font-size: 38px; line-height: 1; color: var(--black); letter-spacing: 1px;
  }
  .contacts { position: absolute; left: 52px; top: 398px; list-style: none; }
  .contacts li {
    display: flex; align-items: center; height: 38px;
    font-size: 24px; color: var(--ink);
  }
  .contacts svg { width: 24px; height: 24px; margin-right: 20px; flex: none; }
  .tagline {
    position: absolute; left: 770px; top: 398px;
    font-family: "Crimson Text", serif; font-style: italic; font-size: 30px;
    line-height: 43px; letter-spacing: 1.5px; color: var(--ink);
  }
</style>
</head>
<body>
<div class="card">
  <svg class="waves" viewBox="0 0 1200 741" width="1200" height="741" aria-hidden="true">
    <defs>
      <linearGradient id="topRed" x1="0" y1="0" x2="0" y2="1">
        <stop offset="0" stop-color="#c3121a"/>
        <stop offset="1" stop-color="#8e0a10"/>
      </linearGradient>
      <linearGradient id="bottomRed" x1="0" y1="0" x2="0" y2="1">
        <stop offset="0" stop-color="#e8141f"/>
        <stop offset="1" stop-color="#c3121a"/>
      </linearGradient>
    </defs>
    <path class="top-edge" fill="var(--black)" d="M0,0 H1200 V242 C1010,226 820,168 620,112 C420,60 200,46 0,54 Z"/>
    <path class="top-band" fill="url(#topRed)" d="M0,0 H1200 V232 C1010,214 820,152 620,98 C420,46 200,34 0,40 Z"/>
    <path class="bottom-edge" fill="var(--black)" d="M0,508 C220,548 500,630 720,686 C860,720 1000,741 1110,741 H0 Z"/>
    <path class="bottom-band" fill="url(#bottomRed)" d="M0,520 C220,562 500,644 720,700 C840,730 960,741 1060,741 H0 Z"/>
  </svg>

  <div class="brand">Tallowbrook<br>Migration</div>

  <h1 class="name"><span class="first">Marla</span><span class="last">Voskuil</span></h1>
  <p class="title">RCIC</p>

  <ul class="contacts">
    <li>
      <svg viewBox="0 0 24 24" aria-hidden="true"><rect x="6" y="1.5" width="12" height="21" rx="2" fill="none" stroke="var(--ink)" stroke-width="2"/><rect x="8" y="4" width="8" height="13" fill="var(--ink)"/></svg>
      (604) 731-5562
    </li>
    <li>
      <svg viewBox="0 0 24 24" aria-hidden="true"><rect x="2" y="5" width="20" height="14" fill="none" stroke="var(--ink)" stroke-width="1.6"/><path d="M2 5 L12 13 L22 5 M2 19 L9.5 11 M22 19 L14.5 11" fill="none" stroke="var(--ink)" stroke-width="1.6"/></svg>
      marla@tallowbrookmigration.example
    </li>
    <li>
      <svg viewBox="0 0 24 24" aria-hidden="true"><g fill="none" stroke="var(--ink)" stroke-width="1.5"><circle cx="12" cy="12" r="10"/><ellipse cx="12" cy="12" rx="4.5" ry="10"/><path d="M2 12 H22 M4 6.5 H20 M4 17.5 H20 M12 2 V22"/></g></svg>
      www.tallowbrookmigration.example
    </li>
  </ul>

  <p class="tagline">"Trusted guidance.<br>Clear pathways.<br>New beginnings."</p>
</div>
</body>
</html>
```